Health and Wellness company needs flyer to promote free seminar

Corelift studio is a health and wellness company that offers an exercise program designed by physical therapists to help relieve pain and improve mobility. Our business is a new concept that is not well understood by the public. In order to promote our business we offer a free seminar where we present information regarding the underlying cause of pain and tightness. During the seminar we also perform a posture screen and movement testing for all participants.

Target Market(s)

Mostly healthy and active women ages 25-65

Industry/Entity Type

Health And Wellness

Font styles to use
Sans Serif

Colors

Designer to choose colors to be used in the design.

Requirements
Must have
• Title: Eliminate Pain and Tightness For Good
• Paragraph: Corelift Studio offers a free 60 minute seminar: "The Busy Walker's Handbook to Stretching and Standing Taller."
• What to Expect:
• • Identify the underlying cause of your pain and mobility issues
• • Expose what gets in the way of you moving and feeling better
• • Learn why traditional exercises don’t help and can actually make the problem worse
• • Reveal what your posture is saying and how that impacts you
• • Experience your muscle imbalances through movement tests
• • Discover the training method that realigns your posture, increases your mobility and reduces your pain
• Call to action: RSVP online at coreliftstudio.com
Nice to have
• Use a relevant image showing a female dealing with tightness in the low back, legs, etc.
• Emphasize that the seminar is FREE.
• Make the call to action prominent.

```html
<!DOCTYPE html>
<html lang="en">
<head>
<meta charset="utf-8">
<title>Corelift Studio – Free Seminar Invitation</title>
<link href="https://fonts.googleapis.com/css2?family=Arimo:wght@400;700&family=Open+Sans:wght@600;700&display=swap" rel="stylesheet">
<style>
  :root {
    --red: #a3181f;
    --white: #ffffff;
    --ink: #1d1d1d;
    --frame: #111111;
    --photo-light: #8a8682;
    --photo-dark: #3b3735;
    --brand: #e9e6ee;
  }
  * { margin: 0; padding: 0; box-sizing: border-box; }
  html, body { width: 800px; height: 1200px; overflow: hidden; background: var(--frame); }
  .flyer {
    position: absolute; left: 24px; top: 28px; width: 750px; height: 1148px;
    background: var(--white); overflow: hidden;
    font-family: "Arimo", Arial, sans-serif;
  }
  .header { position: absolute; left: 0; top: 0; width: 750px; height: 194px; background: var(--red); }
  .header-divider { position: absolute; left: 0; top: 0; }
  .brand { position: absolute; left: 30px; top: 64px; display: flex; align-items: center; gap: 14px; }
  .brand-mark { width: 66px; height: 66px; background: var(--brand); }
  .brand-name { font-weight: 700; font-size: 38px; color: var(--brand); letter-spacing: -0.5px; }
  .invite {
    position: absolute; left: 440px; width: 300px; top: 22px;
    text-align: center; color: var(--white); font-weight: 700; font-size: 50px; line-height: 53px;
  }
  .hero {
    position: absolute; left: 0; top: 194px; width: 750px; height: 468px;
    background: radial-gradient(ellipse at 60% 40%, var(--photo-light), var(--photo-dark) 75%);
  }
  .hero-title {
    position: absolute; left: 20px; top: 214px; width: 380px; text-align: center;
    font-family: "Open Sans", Arial, sans-serif; font-weight: 600; color: var(--white);
    font-size: 43px; line-height: 54px; letter-spacing: -0.5px;
  }
  .cta-panel { position: absolute; left: 0; top: 194px; }
  .cta {
    position: absolute; left: 410px; width: 340px; top: 520px; text-align: center;
    color: var(--white); font-weight: 700; font-size: 28.5px; line-height: 43px; white-space: nowrap;
  }
  .offer-band { position: absolute; left: 0; top: 662px; width: 750px; height: 110px; background: var(--red); }
  .offer {
    position: absolute; left: 300px; width: 420px; top: 672px; text-align: center;
    color: var(--white); font-weight: 700; font-size: 24px; line-height: 33px;
  }
  .offer-quote {
    position: absolute; left: 262px; width: 470px; top: 743px; text-align: center;
    color: var(--white); font-weight: 700; font-size: 11.5px; white-space: nowrap;
  }
  .tabs { position: absolute; left: 0; top: 662px; }
  .key-label {
    position: absolute; left: 28px; top: 738px; color: var(--white);
    font-weight: 700; font-size: 30px;
  }
  .points { position: absolute; left: 30px; top: 780px; width: 720px; list-style: none; }
  .point {
    position: absolute; left: 0; display: flex; align-items: flex-start; gap: 6px;
    color: var(--ink); font-size: 23.5px; line-height: 29px; font-weight: 400; white-space: nowrap;
    -webkit-text-stroke: 0.5px var(--ink);
  }
  .point svg { flex: none; margin-top: 5px; }
  .footer { position: absolute; left: 0; top: 1100px; width: 750px; height: 48px; background: var(--red); }
</style>
</head>
<body>
<main class="flyer">
  <header class="header">
    <svg class="header-divider" width="750" height="194" viewBox="0 0 750 194">
      <polygon points="462,0 469,0 425,194 418,194" fill="#ffffff"/>
    </svg>
    <div class="brand">
      <span class="brand-mark"></span>
      <span class="brand-name">Corelift studio</span>
    </div>
    <h1 class="invite">FREE<br>SEMINER<br>INVITATION</h1>
  </header>

  <section class="hero" role="img" aria-label="Photo of a woman and a man doing barbell squats in a gym"></section>
  <svg class="cta-panel" width="750" height="468" viewBox="0 0 750 468">
    <polygon points="430,290 750,250 750,468 400,468" fill="#1a1a1a" opacity="0.45"/>
  </svg>
  <h2 class="hero-title">ELIMINATE PAIN<br>AND TIGHTNESS<br>FOR GOOD</h2>
  <p class="cta">SIGN UP ONLINE<br>AT CORELIFTSTUDIO.<br>COM/FREE-SEMINER</p>

  <div class="offer-band"></div>
  <svg class="tabs" width="750" height="150" viewBox="0 0 750 150">
    <polygon points="0,38 266,38 244,110 0,110" fill="#ffffff"/>
    <polygon points="0,64 242,64 222,122 0,122" fill="#a3181f"/>
  </svg>
  <p class="offer">CORELIFT STUDIO<br>OFFERS 60 MINUTE SEMINAR</p>
  <p class="offer-quote">“THE BUSY WALKER’S HANDBOOK TO STRETCHING AND STANDING TALLER.”</p>
  <h3 class="key-label">Key points:</h3>

  <ul class="points">
    <li class="point" style="top:10px"><svg width="34" height="20" viewBox="0 0 36 20"><polygon points="0,6 20,6 20,0 34,10 20,20 20,14 0,14" fill="#a3181f"/></svg>Identify the underlying cause of your pain and mobility issues</li>
    <li class="point" style="top:52px"><svg width="34" height="20" viewBox="0 0 36 20"><polygon points="0,6 20,6 20,0 34,10 20,20 20,14 0,14" fill="#a3181f"/></svg>Expose what gets in the way of you moving and feeling better</li>
    <li class="point" style="top:88px"><svg width="34" height="20" viewBox="0 0 36 20"><polygon points="0,6 20,6 20,0 34,10 20,20 20,14 0,14" fill="#a3181f"/></svg>Learn why traditional exercises don’t help and can actually<br>make the problem worse</li>
    <li class="point" style="top:151px"><svg width="34" height="20" viewBox="0 0 36 20"><polygon points="0,6 20,6 20,0 34,10 20,20 20,14 0,14" fill="#a3181f"/></svg>Reveal what your posture is saying and how that impacts you</li>
    <li class="point" style="top:195px"><svg width="34" height="20" viewBox="0 0 36 20"><polygon points="0,6 20,6 20,0 34,10 20,20 20,14 0,14" fill="#a3181f"/></svg>Experience your muscle imbalances through movement tests</li>
    <li class="point" style="top:236px"><svg width="34" height="20" viewBox="0 0 36 20"><polygon points="0,6 20,6 20,0 34,10 20,20 20,14 0,14" fill="#a3181f"/></svg>Discover the training method that realigns your posture,<br>increases your mobility and reduces your pain</li>
  </ul>

  <footer class="footer"></footer>
</main>
</body>
</html>
```